RowPerch.com Business Cards

Logo is attached but does not need to be used. We would prefer if the logo was just on the back of the card. We would like something creative for the front of the card.
Please see our website @ www.RowPerch.com to get a better feel for our company.

Card should include
Name
Title
Phone #
Email Address
Address
Website

```html
<!DOCTYPE html>
<html lang="en">
<head>
<meta charset="utf-8">
<title>RowPerch.com Business Card</title>
<link href="https://fonts.googleapis.com/css2?family=Italianno&family=Parisienne&display=swap" rel="stylesheet">
<style>
  :root {
    --page: #ffffff;
    --card-red: #b9322b;
    --card-edge: #9a9a9a;
    --swoosh-bright: #ff3b30;
    --swoosh-soft: #d8372f;
    --ornament-tone: #a52a24;
    --ink-light: #ffffff;
    --ink-dark: #1a0a08;
    --brand-faint: rgba(140, 28, 24, 0.6);
  }
  * { margin: 0; padding: 0; box-sizing: border-box; }
  html, body {
    width: 1200px; height: 720px; overflow: hidden;
    background: var(--page);
  }
  .business-card {
    position: absolute; left: 40px; top: 40px;
    width: 1120px; height: 640px;
    background: var(--card-red);
    border: 1px solid var(--card-edge);
    overflow: hidden;
    font-family: "Parisienne", cursive;
    color: var(--ink-light);
  }
  .swoosh { position: absolute; inset: 0; width: 100%; height: 100%; }
  .contact { position: absolute; line-height: 1; white-space: nowrap; font-style: normal; }
  .contact-email { left: 20px; top: 14px; font-size: 33px; }
  .contact-phone { right: 30px; top: 16px; font-size: 28px; letter-spacing: 1px; }
  .contact-address { left: 20px; top: 552px; font-size: 30px; line-height: 38px; letter-spacing: 0.5px; }
  .ornament {
    position: absolute; left: 378px; width: 350px; height: 106px;
    background: linear-gradient(90deg, rgba(165,42,36,0) 0%, var(--ornament-tone) 22%, var(--ornament-tone) 78%, rgba(165,42,36,0) 100%);
    border-radius: 40px;
  }
  .ornament-top { top: 92px; }
  .ornament-bottom { top: 399px; }
  .holder-name {
    position: absolute; left: 0; right: 0; top: 278px;
    text-align: center;
    font-family: "Italianno", cursive;
    font-weight: 400;
    font-size: 78px; line-height: 1;
    color: var(--ink-dark);
  }
  .website {
    position: absolute; right: 32px; top: 540px;
    font-size: 50px; line-height: 1;
    color: var(--brand-faint);
    white-space: nowrap;
  }
</style>
</head>
<body>
  <main class="business-card">
    <svg class="swoosh" viewBox="0 0 1120 640" aria-hidden="true">
      <path d="M0 300 C 120 370, 220 420, 330 410 C 470 395, 560 250, 760 215 C 900 195, 1020 205, 1120 212 L1120 250 C 1000 240, 880 240, 760 262 C 580 300, 470 420, 320 425 C 200 428, 90 370, 0 318 Z" fill="var(--swoosh-soft)" opacity="0.7"/>
      <path d="M0 296 C 120 360, 230 400, 330 392 C 470 380, 560 240, 760 212 C 900 195, 1020 205, 1120 210 L1120 218 C 1010 214, 900 212, 770 232 C 580 262, 470 395, 320 405 C 200 412, 90 360, 0 306 Z" fill="var(--swoosh-bright)"/>
      <path d="M560 300 C 680 240, 860 235, 1120 262 L1120 272 C 860 250, 690 258, 560 300 Z" fill="var(--swoosh-soft)"/>
    </svg>

    <p class="contact contact-email">owen.hale@rowperch.com</p>
    <p class="contact contact-phone">Ph : 899 - 555 - 0142</p>

    <div class="ornament ornament-top" role="img" aria-label="Decorative scroll ornament"></div>
    <h1 class="holder-name">Owen Hale, web designer</h1>
    <div class="ornament ornament-bottom" role="img" aria-label="Decorative scroll ornament"></div>

    <address class="contact contact-address">
      214 , 17th St, Suite No.08,<br>
      New York, NY - 10011
    </address>

    <p class="website">www.RowPerch.com</p>
  </main>
</body>
</html>
```